Web Design Project

New website for Aged Care business.

Easy buttons to

1.book appointment

2.request a callback

3.view services

think elderly people using it, or family members

we like the colours of 'tall oak' website

and the middle image and call to action buttons of the pods lawncare website.

we'd like a rotating image similar to the pods lawncare but bigger size.

http://www.talloak-example.org.au/

http://www.podslawncare-example.net/

Target Market(s)

elderly people and families of elderly people with enough money to pay for the services offered.

Industry/Entity Type

Business

Requirements
Must have
• contemporary and clean design

```html
<!DOCTYPE html>
<html lang="en">
<head>
<meta charset="utf-8">
<title>Aged Care</title>
<link rel="stylesheet" href="https://fonts.googleapis.com/css2?family=Arimo:wght@400;700&family=Open+Sans:wght@400;600;700&display=swap">
<style>
:root{
  --navy-dark:#0b2d63;
  --navy:#1a4a8c;
  --navy-light:#3e6fb0;
  --heading-blue:#5b87bf;
  --link-blue:#1d4f91;
  --orange:#ff6a00;
  --side-bg:#f1f1f1;
  --text:#4a4a4a;
  --text-dark:#333;
  --rule:#d9d9d9;
  --white:#fff;
}
*{box-sizing:border-box;margin:0;padding:0}
html,body{width:905px;height:1200px;overflow:hidden;background:var(--white)}
body{position:relative;font-family:"Arimo",Arial,sans-serif;color:var(--text)}
.abs{position:absolute}

/* header */
.header{left:36px;top:4px;width:834px;height:89px;background:linear-gradient(#2c5a9a,var(--navy-dark));}
.logo{left:0;top:14px;width:296px;text-align:center;color:var(--white);font-weight:400;line-height:1}
.logo .small{font-size:16px;display:block}
.logo .big{font-size:44px;display:block;margin-top:2px}
.header-divider{left:296px;top:9px;width:1px;height:72px;background:rgba(255,255,255,.6)}
.access{left:320px;top:10px;color:var(--white);font-size:11px;font-weight:700;line-height:14.3px}
.phone-icon{left:442px;top:10px}
.call{left:472px;top:15px;color:var(--white);font-weight:700;font-size:16px;white-space:nowrap}
.call .number{font-weight:400;font-size:34px;margin-left:5px;vertical-align:-3px}
.callback{right:180px;top:64px;color:var(--white);font-weight:700;font-size:12px;letter-spacing:.3px;white-space:nowrap}
.callback-input{left:660px;top:60px;width:160px;height:19px;background:var(--white);border:1px solid #ccc;font-size:10.5px;color:#ccc;padding:2px 4px;white-space:nowrap;overflow:hidden}

/* nav */
.nav{left:36px;top:102px;width:568px;height:21px;border-radius:11px;background:linear-gradient(var(--navy-light),var(--navy-dark));color:var(--white);font-size:13px;font-weight:700;font-family:"Open Sans",sans-serif;line-height:21px}
.nav span{position:absolute;top:0}
.search-box{left:613px;top:102px;width:166px;height:21px;border:1px solid #9cb4d3;border-radius:11px 0 0 11px;font-size:12px;color:#b6c3d6;padding:2px 19px;font-family:"Open Sans",sans-serif}
.search-btn{left:779px;top:102px;width:90px;height:21px;border-radius:0 11px 11px 0;background:linear-gradient(var(--navy-light),var(--navy-dark));color:var(--white);font-size:13px;font-weight:600;text-align:center;line-height:21px;font-family:"Open Sans",sans-serif}

/* hero */
.hero{top:140px;height:225px;width:337px}
.hero-left{left:82px;background:linear-gradient(90deg,#f4f1ee,#d8cfc6 45%,#b7a7c2 60%,#f4f2f0)}
.hero-right{left:483px;background:linear-gradient(90deg,#eef1f4,#e1c9b5 40%,#a6b6cc 70%,#f2f4f6)}

/* sidebar */
.sidebar{left:35px;top:384px;width:196px;height:691px;background:var(--side-bg)}
.side-head{left:0;top:0;width:196px;height:36px;background:var(--orange);color:var(--white);font-weight:700;font-size:15px;line-height:36px;padding-left:27px;font-family:"Open Sans",sans-serif}
.side-thumb{left:18px;width:107px;height:71px}
.side-title{left:18px;color:var(--link-blue);font-weight:700;font-size:12.5px;font-family:"Open Sans",sans-serif;letter-spacing:.3px}
.side-text{left:18px;width:150px;font-size:10.5px;line-height:14.2px;letter-spacing:.2px}

/* columns */
.col-title{top:385px;width:200px;font-size:29px;line-height:35px;font-weight:400;color:var(--heading-blue)}
.col-img{top:474px;width:196px;height:129px}
.col-text{top:638px;width:200px;font-size:10.6px;line-height:16px;letter-spacing:.1px}
.tile{width:59px;height:59px;border-radius:7px;border:2px solid #ccc}

.rule{left:248px;width:621px;height:1px;background:var(--rule)}

.list-title{top:760px;font-size:15.5px;color:#555;font-weight:400;font-family:"Open Sans",sans-serif;letter-spacing:.6px}
.list{top:785px;list-style:none;font-size:11.5px;letter-spacing:.4px;line-height:21.3px;color:var(--text-dark)}
.list li{padding-left:17px;position:relative}
.list li::before{content:"";position:absolute;left:2px;top:7px;width:7px;height:7px;border-radius:50%;background:radial-gradient(circle at 35% 35%,#bfe0ff,#3a86d6)}

.company{left:696px;top:758px;font-size:21px;font-weight:700;color:#444;font-family:"Open Sans",sans-serif;letter-spacing:.5px}
.contact{left:703px;top:790px;font-size:11.5px;line-height:21.3px;color:var(--text-dark);letter-spacing:.3px;font-style:normal}
.contact b{font-weight:700}

.about-title{left:248px;top:954px;font-size:17px;font-weight:700;color:var(--text-dark);font-family:"Open Sans",sans-serif;letter-spacing:.4px}
.about-text{left:248px;top:983px;width:622px;font-size:10.4px;line-height:20.4px;letter-spacing:.35px;font-family:"Open Sans",sans-serif}

/* footer */
.footer{left:36px;top:1094px;width:834px;height:88px;border-radius:9px;background:linear-gradient(var(--navy-light),var(--navy-dark));color:var(--white);font-size:10.5px;line-height:14.2px;text-align:center;padding-top:15px}
.footer p{width:490px;margin:0 auto}
</style>
</head>
<body>

<header class="abs header">
  <div class="abs logo"><span class="small">YOUR</span><span class="big">LOGO</span></div>
  <div class="abs header-divider"></div>
  <div class="abs access">Accessibility<br>Text Only<br>Resize text<br>A A A<br>Site Map</div>
  <svg class="abs phone-icon" width="28" height="46" viewBox="0 0 28 46" aria-hidden="true">
    <path d="M20 2c-6 2-12 8-14 18s1 20 6 24l6-6c-3-3-5-9-4-15s4-10 8-12z" fill="#d7dde6" stroke="#fff" stroke-width="1.5"/>
    <rect x="16" y="1" width="10" height="12" rx="3" fill="#eef1f5"/>
    <rect x="9" y="36" width="10" height="10" rx="3" fill="#eef1f5"/>
  </svg>
  <div class="abs call">Call us today<span class="number">0800 555 0142</span></div>
  <div class="abs callback">Or we can call you:</div>
  <div class="abs callback-input">Enter your telephone number</div>
</header>

<nav class="abs nav">
  <span style="left:21px">Book Appointment</span>
  <span style="left:160px">|</span>
  <span style="left:189px">Request Callback</span>
  <span style="left:320px">|</span>
  <span style="left:349px">View Services</span>
  <span style="left:457px">|</span>
  <span style="left:486px">About Us</span>
</nav>
<div class="abs search-box">Search</div>
<div class="abs search-btn">Search</div>

<div class="abs hero hero-left" role="img" aria-label="Photo of a carer sitting with an elderly man on a sofa"></div>
<div class="abs hero hero-right" role="img" aria-label="Photo of an elderly man with his family"></div>

<aside class="abs sidebar">
  <div class="abs side-head">Lorem Ipsum</div>

  <div class="abs side-thumb" style="top:40px;background:linear-gradient(120deg,#e8dccf,#cbbfae,#f0ece6)" role="img" aria-label="Photo of a carer with an elderly woman"></div>
  <div class="abs side-title" style="top:117px">Lorem ipsum</div>
  <p class="abs side-text" style="top:144px">Lorem ipsum dolor sit amet, consectetur adipisicing elit, sed do eiusmod tempor incididunt ut labore et dolore magna aliqua. Ut enim ad minim veniam, quis nostrud</p>

  <div class="abs side-thumb" style="top:255px;background:linear-gradient(120deg,#c9b2a4,#e6dcd6,#b98f78)" role="img" aria-label="Photo of an elderly man and a young woman"></div>
  <div class="abs side-title" style="top:334px">Lorem ipsum</div>
  <p class="abs side-text" style="top:363px">Lorem ipsum dolor sit amet, consectetur adipisicing elit, sed do eiusmod tempor incididunt ut labore et dolore magna aliqua. Ut enim ad minim veniam, quis nostrud</p>

  <div class="abs side-thumb" style="top:470px;background:linear-gradient(120deg,#e4c39a,#d9b38f,#a9c6d8)" role="img" aria-label="Photo of an elderly woman with her daughter"></div>
  <div class="abs side-title" style="top:555px">Lorem ipsum</div>
  <p class="abs side-text" style="top:593px">Lorem ipsum dolor sit amet, consectetur adipisicing elit, sed do eiusmod tempor incididunt ut labore et dolore magna aliqua. Ut enim ad minim veniam, quis nostrud</p>
</aside>

<h2 class="abs col-title" style="left:248px">Book Appointment</h2>
<h2 class="abs col-title" style="left:461px">Request Callback</h2>
<h2 class="abs col-title" style="left:674px">View Our Services</h2>

<div class="abs col-img" style="left:248px;background:linear-gradient(135deg,#7a5a46,#e9e1d8 40%,#d9c9b9 80%,#a67f63)" role="img" aria-label="Photo of a hand writing in an appointment diary"></div>
<div class="abs col-img" style="left:461px;background:linear-gradient(90deg,#f2f4f7,#e3e7ee 40%,#d8c9b8 60%,#eef1f5)" role="img" aria-label="Photo of a doctor on the telephone"></div>

<div class="abs tile" style="left:676px;top:474px;background:linear-gradient(#4b7cf0,#0a2bb5)" role="img" aria-label="Service icon: in-home assistance"></div>
<div class="abs tile" style="left:745px;top:474px;background:linear-gradient(#666,#111)" role="img" aria-label="Service icon: social activities"></div>
<div class="abs tile" style="left:814px;top:474px;background:linear-gradient(#6fd33c,#137a0f)" role="img" aria-label="Service icon: personal care"></div>
<div class="abs tile" style="left:676px;top:544px;background:linear-gradient(#d8283a,#6d0511)" role="img" aria-label="Service icon: group outings"></div>
<div class="abs tile" style="left:745px;top:544px;background:linear-gradient(#b23ac7,#4a0a5c)" role="img" aria-label="Service icon: exercise classes"></div>
<div class="abs tile" style="left:814px;top:544px;background:linear-gradient(#ffb02e,#e05400)" role="img" aria-label="Service icon: community dining"></div>

<p class="abs col-text" style="left:248px">Lorem ipsum dolor sit amet, consectetur adipisicing elit, sed do eiusmod tempor incididunt ut labore et dolore magna aliqua. Ut enim ad minim veniam, quis nostrud exercitation ullamco laboris nisi ut aliquip ex ea commodo consequat.</p>
<p class="abs col-text" style="left:461px">Lorem ipsum dolor sit amet, consectetur adipisicing elit, sed do eiusmod tempor incididunt ut labore et dolore magna aliqua. Ut enim ad minim veniam, quis nostrud exercitation ullamco laboris nisi ut aliquip ex ea commodo consequat.</p>
<p class="abs col-text" style="left:674px">Lorem ipsum dolor sit amet, consectetur adipisicing elit, sed do eiusmod tempor incididunt ut labore et dolore magna aliqua. Ut enim ad minim veniam, quis nostrud exercitation ullamco laboris nisi ut aliquip ex ea commodo consequat.</p>

<div class="abs rule" style="top:748px"></div>

<h3 class="abs list-title" style="left:248px">Lorem ipsum</h3>
<ul class="abs list" style="left:250px"><li>Dolor sit</li><li>Amet</li><li>Consectetur</li><li>Adipisicing</li><li>Elit sed do</li><li>Eiusmod tempor</li><li>Incididunt ut</li></ul>
<h3 class="abs list-title" style="left:402px">Lorem ipsum</h3>
<ul class="abs list" style="left:404px"><li>Dolor sit</li><li>Amet</li><li>Consectetur</li><li>Adipisicing</li><li>Elit sed do</li><li>Eiusmod tempor</li><li>Incididunt ut</li></ul>
<h3 class="abs list-title" style="left:554px">Lorem ipsum</h3>
<ul class="abs list" style="left:556px"><li>Dolor sit</li><li>Amet</li><li>Consectetur</li><li>Adipisicing</li><li>Elit sed do</li><li>Eiusmod tempor</li><li>Incididunt ut</li></ul>

<h3 class="abs company">Duis Aute Ltd</h3>
<address class="abs contact">12 Dolor &nbsp;Reprehenderit<br>In Voluptate 1234<br>Phone: (00) 1234 5678<br>Fax: (00) 1234 5678<br>Email: &nbsp;<b>click here</b></address>

<div class="abs rule" style="top:943px"></div>

<h3 class="abs about-title">Lorem Ipsum</h3>
<p class="abs about-text">Lorem ipsum dolor sit amet, consectetur adipisicing elit, sed do eiusmod tempor incididunt ut labore et dolore magna aliqua. Ut enim ad minim veniam, quis nostrud exercitation ullamco laboris nisi ut aliquip ex ea commodo consequat. Duis aute irure dolor in reprehenderit in voluptate velit esse cillum dolore eu fugiat nulla pariatur. Excepteur sint occaecat cupidatat non proident, sunt in culpa qui officia deserunt mollit anim id est laborum.</p>

<footer class="abs footer">
  <p>&copy;Aged Care 2012 All Rights Reserved<br>Lorem ipsum dolor sit amet, consectetur adipisicing elit, sed do eiusmod tempor incididunt ut labore et dolore magna aliqua. Ut enim ad minim veniam, quis nostrud exercitation ullamco laboris nisi ut aliquip ex ea commodo consequat.</p>
</footer>

</body>
</html>
```